Corvane Electronics, Inc. Business card

Incorporate a globe.
We repair electronics, sell electronic parts, and we recycle electronics. We've been in business since 1982. A technology feel to the card is preferred. I want to be able to give this card to a client from different industries and make it relate-able. I don't have a logo that I've been partial to in the past. It is not necessary in this case.

Target Market(s)

Consumer, Industrial, Business, Medical

Industry/Entity Type

Business

Contact Information for Business Card

4518 Maple Crest Blvd. Dallas, TX 75207
214-555-0187 main 214-555-0143 fax
Paul Bredesen VP

Font styles to use
Serif

Requirements
Must have
• Technology feel
Nice to have
• Metallic look
Should not have
• no pastel colors

```html
<!DOCTYPE html>
<html lang="en">
<head>
<meta charset="utf-8">
<title>Corvane Electronics, Inc. – Business Card</title>
<link rel="stylesheet" href="https://fonts.googleapis.com/css2?family=Open+Sans:wght@700&display=swap">
<style>
  :root {
    --card-bg: #0c0c0d;
    --accent: #5bbfdb;
    --text: #ffffff;
  }
  html, body {
    margin: 0;
    padding: 0;
    width: 1200px;
    height: 686px;
    overflow: hidden;
    background: var(--card-bg);
  }
  .card {
    position: relative;
    width: 1200px;
    height: 686px;
    background: var(--card-bg);
    font-family: "Open Sans", Arial, sans-serif;
    font-weight: 700;
    color: var(--text);
  }
  .brand-name {
    position: absolute;
    top: 160px;
    left: 0;
    width: 100%;
    margin: 0;
    text-align: center;
    font-size: 64px;
    line-height: 1;
    letter-spacing: 1px;
    color: var(--accent);
  }
  .person {
    position: absolute;
    left: 80px;
    top: 404px;
    margin: 0;
    font-size: 66px;
    line-height: 1;
    letter-spacing: -0.5px;
    white-space: nowrap;
  }
  .person-rule {
    position: absolute;
    left: 80px;
    top: 474px;
  }
  .contact-tree {
    position: absolute;
    left: 700px;
    top: 340px;
  }
  .contact-line {
    position: absolute;
    left: 840px;
    margin: 0;
    white-space: nowrap;
  }
  .contact-line.phone { top: 340px; font-size: 43px; line-height: 1.15; }
  .contact-line.fax   { top: 414px; font-size: 43px; line-height: 1.15; }
  .contact-line.address { top: 503px; font-size: 29px; line-height: 38px; }
</style>
</head>
<body>
  <div class="card">
    <h1 class="brand-name">Corvane Electronics</h1>

    <p class="person">Paul Bredesen VP</p>
    <svg class="person-rule" width="400" height="16" viewBox="0 0 400 16" aria-hidden="true">
      <line x1="2" y1="8" x2="392" y2="8" stroke="var(--accent)" stroke-width="3" stroke-linecap="round"/>
      <circle cx="392" cy="8" r="5" fill="var(--accent)"/>
    </svg>

    <svg class="contact-tree" width="135" height="220" viewBox="0 0 135 220" aria-hidden="true">
      <g stroke="var(--accent)" stroke-width="3" fill="none" stroke-linecap="round">
        <line x1="14" y1="18" x2="14" y2="194"/>
        <line x1="14" y1="18" x2="45" y2="18"/>
        <line x1="14" y1="98" x2="45" y2="98"/>
        <line x1="14" y1="194" x2="45" y2="194"/>
      </g>
      <g fill="var(--accent)">
        <circle cx="45" cy="18" r="5"/>
        <circle cx="45" cy="98" r="5"/>
        <circle cx="45" cy="194" r="5"/>
      </g>
      <g class="icon-mobile" stroke="var(--accent)" stroke-width="3.5" fill="none">
        <rect x="86" y="-3" width="26" height="44" rx="5"/>
        <line x1="95" y1="34" x2="103" y2="34" stroke-linecap="round"/>
      </g>
      <g class="icon-fax" fill="var(--accent)">
        <rect x="88" y="80" width="22" height="14" rx="2" fill="none" stroke="var(--accent)" stroke-width="3"/>
        <line x1="92" y1="85" x2="106" y2="85" stroke="var(--accent)" stroke-width="2"/>
        <line x1="92" y1="89" x2="106" y2="89" stroke="var(--accent)" stroke-width="2"/>
        <path d="M80 104 q19 -12 38 0 v10 q0 4 -4 4 h-6 v-6 h-18 v6 h-6 q-4 0 -4 -4 z"/>
      </g>
      <path class="icon-pin" d="M99 168 a14 14 0 0 1 14 14 c0 12 -14 30 -14 30 c0 0 -14 -18 -14 -30 a14 14 0 0 1 14 -14 z"
            fill="none" stroke="var(--accent)" stroke-width="3.5" stroke-linejoin="round"/>
      <circle cx="99" cy="182" r="5" fill="none" stroke="var(--accent)" stroke-width="3"/>
    </svg>

    <p class="contact-line phone">214-555-0187</p>
    <p class="contact-line fax">214-555-0143</p>
    <p class="contact-line address">4518 Maple Crest Blvd.<br>Dallas, TX 75207</p>
  </div>
</body>
</html>
```